Craft Portuguese Gin Distillery launching new gin into international market

We are going to launch two new gins:
1. An aged version of the Volka Sereno, one that already exists - aged in port casks. This will be a 500ml bottle. Bottle not defined yet - Check www.sipvolka.example
2. A new gin with a lower ABV (lower strength), to satisfy both connoisseurs and "ordinary"; customers. We want to stay with the branding line. The label must appeal to the customer to try the gin, must stand out on a shelf that is full of other spirits. We want to pass on the idea of a premium gin. No botle selected yet. For this gin we may use only a label or a complete decorated bottle. Take care of the legal demands that have to go onto the label - we can help with this later on.
Notes:
- The distillery's name is Volka - Premium Spirits (logo attached)
- Our first gin is called Volka Sereno (logo attached)
- No names selected for either of these gins;
- We have a moto that we would like to see on the bottle:
"Drink to remember, not to forget!";
- Our gins have a unique botanical that is fig tree bark, we are portuguese and we are very fond of the fig image attached.
- Attached we send some documents where you can learn about the story of the gin and also for you to get to know us little better.
- If you wish to suggest a bottle, please look-up these two web sites:
https://www.brimcraft.example/en
https://www.lumavessel.example/
Please contact us for any further information.
Thank you

Target Market(s)

Spirits worldwide

Colors

Designer to choose colors to be used in the design.

Requirements
Must have
• Mandatory Legal information for spirit drinks
• Place for:
• - Producer / bottler (name and addres)
• - Origin fo the product - Product from Portugal
• - ABV and Capacity
• - Type of product: "Londo Dry Gin"
Nice to have
• - We have a moto that we would like to see on the bottle:
• "quot;Drink to remember, not to forget!";
• - Our gins have a unique botanical that is fig tree bark, we are portuguese and we are very fond of the fig image attached.

```html
<!DOCTYPE html>
<html lang="en">
<head>
<meta charset="utf-8">
<title>Volka – Premium Gin Labels</title>
<link href="https://fonts.googleapis.com/css2?family=Montserrat:wght@500;600;700;800&display=swap" rel="stylesheet">
<style>
  :root {
    --page-bg: #eef0f8;
    --label-blue: #4a76a6;
    --label-blue-deep: #3d6696;
    --botanical-dark: #2f5585;
    --navy: #1f3f73;
    --white: #ffffff;
    --stat-box: rgba(31, 63, 115, 0.35);
  }
  * { box-sizing: border-box; margin: 0; padding: 0; }
  html, body { width: 1200px; height: 1200px; overflow: hidden; }
  body {
    background: radial-gradient(circle at 50% 50%, #ffffff 0%, var(--page-bg) 100%);
    font-family: "Montserrat", sans-serif;
    color: var(--white);
    position: relative;
  }
  .label {
    position: absolute;
    top: 227px;
    width: 400px;
    height: 746px;
    background: var(--label-blue);
    overflow: hidden;
  }
  .label--front { left: 150px; }
  .label--back { left: 650px; }

  .botanical-art {
    position: absolute;
    inset: 0;
    background:
      radial-gradient(ellipse 70% 45% at 75% 30%, var(--botanical-dark) 0%, transparent 70%),
      radial-gradient(ellipse 60% 40% at 20% 75%, var(--botanical-dark) 0%, transparent 70%),
      linear-gradient(160deg, var(--label-blue) 0%, var(--label-blue-deep) 100%);
    opacity: 0.9;
  }
  .label--back .botanical-art {
    background:
      radial-gradient(ellipse 55% 35% at 60% 55%, var(--botanical-dark) 0%, transparent 70%),
      var(--label-blue);
    opacity: 0.7;
  }

  .brand-box {
    position: absolute;
    left: 91px; top: 36px;
    width: 231px; height: 206px;
    background: var(--white);
    display: flex; flex-direction: column;
    align-items: center; justify-content: center;
    gap: 18px;
  }
  .brand-name {
    font-weight: 700;
    font-size: 64px;
    color: var(--label-blue);
    letter-spacing: -1px;
    line-height: 1;
  }
  .brand-tagline {
    font-weight: 800;
    font-size: 11px;
    color: var(--label-blue);
    letter-spacing: 0.5px;
  }
  .grade-band {
    position: absolute;
    left: 91px; top: 246px;
    width: 231px; height: 43px;
    background: var(--navy);
    display: flex; align-items: center; justify-content: center;
    font-weight: 700; font-size: 24px;
  }
  .motto {
    position: absolute;
    left: 91px; top: 336px;
    font-weight: 800;
    font-size: 36px;
    line-height: 45px;
    letter-spacing: 0.3px;
  }
  .stat {
    position: absolute;
    top: 572px; height: 96px;
    background: var(--stat-box);
    display: flex; flex-direction: column;
    align-items: center; justify-content: center;
  }
  .stat--abv { left: 99px; width: 94px; }
  .stat--volume { left: 206px; width: 112px; }
  .stat-value { font-weight: 800; font-size: 38px; line-height: 1; }
  .stat-unit { font-weight: 500; font-size: 22px; margin-top: 6px; }
  .product-type {
    position: absolute;
    left: 0; right: 0; top: 692px;
    text-align: center;
    font-weight: 700; font-size: 13px;
    letter-spacing: 0.2px;
  }

  .legal-copy {
    position: absolute;
    left: 35px; top: 62px;
    width: 340px;
  }
  .legal-section + .legal-section { margin-top: 40px; }
  .legal-heading { font-weight: 700; font-size: 20px; margin-bottom: 14px; }
  .legal-body { font-weight: 600; font-size: 19px; line-height: 25px; }
</style>
</head>
<body>

  <section class="label label--front" aria-label="Front label">
    <div class="botanical-art" role="img" aria-label="Engraved fig tree branch with leaves and figs in deep blue"></div>
    <div class="brand-box">
      <span class="brand-name">Volka</span>
      <span class="brand-tagline">BE BOLD, GO STRONG</span>
    </div>
    <div class="grade-band">PREMIUM</div>
    <h1 class="motto">DRINK TO<br>REMEMBER<br>NOT TO<br>FORGET</h1>
    <div class="stat stat--abv">
      <span class="stat-value">58</span>
      <span class="stat-unit">ABV</span>
    </div>
    <div class="stat stat--volume">
      <span class="stat-value">500</span>
      <span class="stat-unit">ML</span>
    </div>
    <p class="product-type">LONDO DRY GIN FROM PORTUGAL</p>
  </section>

  <section class="label label--back" aria-label="Back label">
    <div class="botanical-art" role="img" aria-label="Faint fig leaf engraving in blue"></div>
    <div class="legal-copy">
      <div class="legal-section">
        <h2 class="legal-heading">Legal information</h2>
        <p class="legal-body">Lorem ipsum dolor sit amet, consectetur adipisicing elit, sed do eiusmod tempor incididunt ut labore et dolore magna aliqua. Lorem ipsum dolor sit amet, consectetur adipisicing elit, sed do eiusmod tempor incididunt ut labore et dolore magna aliqua. Incididunt ut labore et dolore magna aliqua.</p>
      </div>
      <div class="legal-section">
        <h2 class="legal-heading">Ingredients</h2>
        <p class="legal-body">Lorem ipsum dolor sit amet, consectetur adipisicing elit, sed do eiusmod tempor incididunt</p>
      </div>
      <div class="legal-section">
        <h2 class="legal-heading">Producer / bottler</h2>
        <p class="legal-body">Lorem ipsum dolor sit amet, consectetur adipisicing elit, sed do eiusmod tempor incididunt</p>
      </div>
    </div>
  </section>

</body>
</html>
```